Business card for a boutique travel agency VELARIEN

we need a business card design - double sided. We would like to have a very elegant, sophisticated but modern design. we are travel consultants and our business focus is Europe, mainly the city of Paris. We would like to receive designs in white and silver, black color but if you are confident that we should pick up a color to make it different and more beautful...go ahead! We are going to give business cards to our clients and business partners. It is important to be perceived as elegant, modern and trustful. Please check jpg references.

Target Market(s)

Velarien primary clients are individuals, couples and affinity groups of high-net-worth who travel for leisure at least once per year. Seeking the ultimate travel experience, the target clients demand the finest quality activities and accommodations accompanied by a superior level of service.

Industry/Entity Type

Travel Industry

Contact Information for Business Card

Lucinda Farrow
- lucinda@velarien-example.com
- +55 11 98347.2516
- velarien-example.com
- unique travel experiences (we would like to see this signature printed as a detail)

Font styles to use
Sans Serif

Colors

Designer to choose colors to be used in the design.

Requirements
Must have
• the Velarien logo that I have attached
Nice to have
• we would like to have some nice detail, something different that shows that we care about,... we are detail oriented.
Should not have
• decorative fonts

```html
<!DOCTYPE html>
<html lang="en">
<head>
<meta charset="utf-8">
<title>Velarien — Business Card</title>
<link rel="stylesheet" href="https://fonts.googleapis.com/css2?family=Josefin+Sans:wght@300&family=Open+Sans:wght@400&family=Oswald:wght@500&display=swap">
<style>
  :root {
    --backdrop: #6b4530;
    --card: #1a1a1a;
    --silver: #9a9a9a;
    --tagline: #8a8a8a;
    --ink: #ffffff;
    --rule: #d8d8d8;
  }
  * { margin: 0; padding: 0; box-sizing: border-box; }
  html, body { width: 1200px; height: 1000px; overflow: hidden; }
  body { background: var(--backdrop); position: relative; }

  .card {
    position: absolute;
    left: 266px;
    width: 666px;
    height: 397px;
    background: var(--card);
  }
  .card--front { top: 74px; }
  .card--back { top: 533px; }

  .wordmark {
    position: absolute;
    top: 172px;
    left: 0;
    width: 100%;
    text-align: center;
    font-family: "Josefin Sans", sans-serif;
    font-weight: 300;
    font-size: 42px;
    letter-spacing: 0.32em;
    padding-left: 0.32em;
    color: var(--silver);
    line-height: 1;
  }
  .tagline {
    position: absolute;
    top: 349px;
    left: 0;
    width: 100%;
    text-align: center;
    font-family: "Open Sans", sans-serif;
    font-size: 16px;
    color: var(--tagline);
  }

  .holder-name {
    position: absolute;
    right: 375px;
    top: 178px;
    font-family: "Oswald", sans-serif;
    font-weight: 500;
    font-size: 29px;
    letter-spacing: -0.01em;
    color: var(--ink);
    text-transform: uppercase;
    line-height: 1;
    transform: scaleX(0.9);
    transform-origin: right center;
  }
  .divider {
    position: absolute;
    left: 318px;
    top: 170px;
    width: 1.5px;
    height: 55px;
    background: var(--rule);
  }
  .contact-list {
    position: absolute;
    left: 342px;
    top: 164px;
    list-style: none;
    font-family: "Open Sans", sans-serif;
    font-size: 15.5px;
    color: var(--ink);
    line-height: 22.5px;
  }
  .contact-item { display: flex; align-items: center; gap: 6px; }
  .contact-icon { width: 14px; height: 14px; fill: var(--ink); flex: none; }
</style>
</head>
<body>
  <section class="card card--front">
    <div class="wordmark">VELARIEN</div>
    <p class="tagline">Unique Travel Experiences</p>
  </section>

  <section class="card card--back">
    <h1 class="holder-name">Lucinda Farrow</h1>
    <div class="divider"></div>
    <ul class="contact-list">
      <li class="contact-item">
        <svg class="contact-icon" viewBox="0 0 16 16" aria-hidden="true">
          <path d="M1 6c0-2 3-3 7-3s7 1 7 3v1h-3.5V5.5h-7V7H1z"/>
          <path d="M4 8h8l2 6H2z"/>
        </svg>
        <span>+55 11 98347.2516</span>
      </li>
      <li class="contact-item">
        <svg class="contact-icon" viewBox="0 0 16 16" aria-hidden="true">
          <path d="M1 3h14v1.2L8 9 1 4.2z"/>
          <path d="M1 5.8l7 4.8 7-4.8V13H1z"/>
        </svg>
        <span>lucinda@velarien-example.com</span>
      </li>
      <li class="contact-item">
        <svg class="contact-icon" viewBox="0 0 16 16" aria-hidden="true">
          <circle cx="7" cy="7" r="6" fill="none" stroke="#fff" stroke-width="1.6"/>
          <path d="M1 7h12M7 1c-2.5 3-2.5 9 0 12M7 1c2.5 3 2.5 9 0 12" fill="none" stroke="#fff" stroke-width="1.1"/>
          <path d="M9 9l6 2.5-2.5 1-1 2.5z"/>
        </svg>
        <span>www.velarien-example.com</span>
      </li>
    </ul>
  </section>
</body>
</html>
```